Consulting services and software brochure

We need a brochure designed that would ideally work with our logo and highlight a few of our consulting services and a couple products we offer. Our industry is real estate technology and we focus on consulting services for third party software systems. We would like the design to work well with our logo colors although we are open to changing either the blue or the orange to white in a design. The final design should clearly highlight our service options in an easy to read way while also leaving plenty of room to insert a lot of text on each service

What we like about our current design: it incorporates our colors well and has lots of room for text on each service, the two product offerings, and a couple testimonials from our clients

What we don’t like: It’s very busy and doesn’t highlight our offerings without a lot of reading. We also think it could have better layout, be much more polished and interesting visually (this was not designed by a professional).

Please provide source file compatible with Photoshop.

We are impressed with the designs so far and have made the payment guaranteed for this project. We will be starting to provide feedback early next week as we review internally.

Regarding size: We are open to a multi-page brochure or an 8 1/2 x 11, square shape, etc. After reviewing the designs we have decided the tri-folds seem to look too busy though on a standard piece of paper. Also, there's a good chance whatever designer we choose we will also hire to do another option in a different size/length so please don't worry either way too much about that.

Thanks for the great submissions so far!

Reason: Hi - we're extending the deadline a week since a few people providing input have been out this week for Passover and Good Friday. Thank you for your understanding.

Reason: Hi - we've settled on a designer and are now refining the brochure. Thank you everyone for your time and effort.

Real Estate

```html
<!DOCTYPE html>
<html lang="en">
<head>
<meta charset="utf-8">
<title>Our Services</title>
<link rel="stylesheet" href="https://fonts.googleapis.com/css2?family=Roboto+Slab:wght@600;700&family=Roboto:wght@300;400&display=swap">
<style>
  :root {
    --bg: #363230;
    --tan: #e8a456;
    --sky: #1ec3dc;
    --ember: #e57843;
    --ink: #ffffff;
    --row-h: 103px;
    --row-gap: 12px;
    --top: 186px;
  }
  * { box-sizing: border-box; margin: 0; padding: 0; }
  html, body { width: 848px; height: 1200px; overflow: hidden; }
  body { background: var(--bg); }
  .brochure-page {
    position: relative;
    width: 848px;
    height: 1200px;
    background: var(--bg);
    overflow: hidden;
  }
  .page-title {
    position: absolute;
    left: 66px;
    top: 112px;
    font-family: "Roboto", sans-serif;
    font-weight: 400;
    font-size: 46px;
    line-height: 1.2;
    letter-spacing: 0.5px;
    color: var(--ink);
  }
  .service-list { list-style: none; }
  .service-row {
    position: absolute;
    left: 0;
    width: 848px;
    height: var(--row-h);
  }
  .service-number,
  .service-name {
    position: absolute;
    top: 0;
    height: var(--row-h);
    display: flex;
    align-items: center;
    justify-content: center;
  }
  .service-number {
    background: var(--tan);
    font-family: "Roboto", sans-serif;
    font-weight: 300;
    font-size: 104px;
    line-height: 1;
    color: transparent;
    -webkit-text-stroke: 1.3px var(--ink);
  }
  .service-name {
    font-family: "Roboto Slab", serif;
    font-weight: 600;
    font-size: 23px;
    line-height: 1.3;
    text-align: center;
    color: var(--ink);
    padding: 0 20px;
  }
  .service-row--left .service-number { left: 0; width: 257px; }
  .service-row--left .service-name { left: 279px; width: 491px; background: var(--sky); }
  .service-row--right .service-name { left: 59px; width: 491px; background: var(--ember); }
  .service-row--right .service-number { left: 571px; width: 277px; }
  .service-row:nth-child(1) { top: calc(var(--top) + 0 * (var(--row-h) + var(--row-gap))); }
  .service-row:nth-child(2) { top: calc(var(--top) + 1 * (var(--row-h) + var(--row-gap))); }
  .service-row:nth-child(3) { top: calc(var(--top) + 2 * (var(--row-h) + var(--row-gap))); }
  .service-row:nth-child(4) { top: calc(var(--top) + 3 * (var(--row-h) + var(--row-gap))); }
  .service-row:nth-child(5) { top: calc(var(--top) + 4 * (var(--row-h) + var(--row-gap))); }
  .service-row:nth-child(6) { top: calc(var(--top) + 5 * (var(--row-h) + var(--row-gap))); }
  .service-row:nth-child(7) { top: calc(var(--top) + 6 * (var(--row-h) + var(--row-gap))); }
  .service-row:nth-child(8) { top: calc(var(--top) + 7 * (var(--row-h) + var(--row-gap))); }
</style>
</head>
<body>
  <main class="brochure-page">
    <h1 class="page-title">OUR SERVICES</h1>
    <ol class="service-list">
      <li class="service-row service-row--left">
        <span class="service-number">1</span>
        <span class="service-name">PROCESS IMPROVEMENT</span>
      </li>
      <li class="service-row service-row--right">
        <span class="service-name">SYSTEM IMPLEMENTATION</span>
        <span class="service-number">2</span>
      </li>
      <li class="service-row service-row--left">
        <span class="service-number">3</span>
        <span class="service-name">DATA CONVERSION</span>
      </li>
      <li class="service-row service-row--right">
        <span class="service-name">CUSTOMIZATION</span>
        <span class="service-number">4</span>
      </li>
      <li class="service-row service-row--left">
        <span class="service-number">5</span>
        <span class="service-name">HELP DESK SUPPORT</span>
      </li>
      <li class="service-row service-row--right">
        <span class="service-name">TRAINING</span>
        <span class="service-number">6</span>
      </li>
      <li class="service-row service-row--left">
        <span class="service-number">7</span>
        <span class="service-name">SPREADSHEET ANALYTICS</span>
      </li>
      <li class="service-row service-row--right">
        <span class="service-name">DASHBOARDS/BUSINESS<br>INTELLIGENCE</span>
        <span class="service-number">8</span>
      </li>
    </ol>
  </main>
</body>
</html>
```